Three Ebook Covers for Short Stories

Three Ebook cover designs for 3 short stories (all linked) psychological thriller. I like clean crisp images. Perhaps with an imagine of eyes/part of face - white woman, 29, thin, brown eyes, short bob hair. I like gritty, moody, raw type of images. I dont mind the same image being used on three covers providing there are differences (ie slight variation in colour of book). Colours I prefer red, burgundy, black, grey, white. My website shows off the type of colours I prefer. www.lydiakbarnes-author.net
Branding is important.

Target Market(s)

Adult. Moth in Attic, Lost Field, type of readers.

Industry/Entity Type

Book Publisher

Font styles to use
Sans Serif
Other font styles liked:
• fonts used on thriller novels

Requirements
Must have
• Author Name: Lydia K Barnes
• Short Story as Part of Title
• Short Story 1: Title - First Crow
• Short Story 2: Title - Second Crow
• Short Story 3: Title - Third Crow
• Branding is important so they must look like they are a set.
• A font which is aligned to thriller type novels
• Colours aligned to my website - red, burgundy, white, grey, black.
Nice to have
• I don't mind a black and white type photo imagine.
Should not have
• n/a

```html
<!DOCTYPE html>
<html lang="en">
<head>
<meta charset="UTF-8">
<title>Short Story Covers – Lydia K Barnes</title>
<link rel="stylesheet" href="https://fonts.googleapis.com/css2?family=Rubik+Distressed&display=swap">
<style>
  :root {
    --page-bg: #ffffff;
    --ink-black: #050505;
    --ink-white: #f2f2f2;
    --cover-black: #000000;
    --cover-burgundy: #680708;
    --cover-charcoal: #2a2a2a;
    --band-white: #ffffff;
    --band-grey: #dcdcdc;
    --shadow: rgba(0, 0, 0, 0.35);
  }
  * { margin: 0; padding: 0; box-sizing: border-box; }
  html, body {
    width: 1200px;
    height: 600px;
    overflow: hidden;
    background: var(--page-bg);
  }
  .cover-set {
    position: relative;
    width: 1200px;
    height: 600px;
  }
  .cover {
    position: absolute;
    top: 24px;
    width: 355px;
    height: 504px;
    overflow: hidden;
    box-shadow: 1px 2px 5px var(--shadow);
    font-family: "Rubik Distressed", "Arial Narrow", sans-serif;
  }
  .cover--one   { left: 44px;  background: var(--cover-black); }
  .cover--two   { left: 418px; background: var(--cover-burgundy); }
  .cover--three { left: 799px; background: var(--cover-charcoal); }

  .cover__photo {
    position: absolute;
    top: 0;
    left: 0;
    width: 100%;
    height: 215px;
  }
  .cover--one .cover__photo {
    background:
      linear-gradient(to bottom, transparent 55%, var(--cover-black) 100%),
      linear-gradient(to right, #000 0%, transparent 30%, transparent 85%, #000 100%),
      radial-gradient(ellipse 42% 70% at 52% 30%, #9a9a9a 0%, #5e5e5e 35%, #2a2a2a 65%, #0a0a0a 100%);
  }
  .cover--two .cover__photo {
    background:
      linear-gradient(to bottom, transparent 55%, var(--cover-burgundy) 100%),
      linear-gradient(to right, #1a0000 0%, transparent 30%, transparent 85%, #1a0000 100%),
      radial-gradient(ellipse 42% 70% at 52% 30%, #d06060 0%, #9a3030 35%, #4a0a0a 65%, #200000 100%);
  }
  .cover--three .cover__photo {
    background:
      linear-gradient(to bottom, transparent 55%, var(--cover-charcoal) 100%),
      linear-gradient(to right, #000 0%, transparent 30%, transparent 85%, #000 100%),
      radial-gradient(ellipse 42% 70% at 52% 30%, #9a9a9a 0%, #5e5e5e 35%, #2a2a2a 65%, #0a0a0a 100%);
  }

  .cover__author {
    position: absolute;
    top: 214px;
    right: 30px;
    font-size: 20px;
    line-height: 1;
    letter-spacing: 1.5px;
    text-transform: uppercase;
    color: var(--ink-white);
    white-space: nowrap;
    transform: scale(0.95, 1.1);
    transform-origin: right top;
  }
  .cover__series {
    position: absolute;
    left: 0;
    right: 0;
    top: 364px;
    text-align: center;
    font-size: 42px;
    line-height: 1;
    letter-spacing: 2px;
    text-transform: uppercase;
    color: var(--ink-white);
    white-space: nowrap;
    transform: scale(0.8, 1.15);
  }
  .cover__title-band {
    position: absolute;
    left: 0;
    right: 0;
    bottom: 0;
    height: 92px;
    display: flex;
    align-items: center;
    justify-content: center;
    background: var(--band-white);
  }
  .cover--three .cover__title-band { background: var(--band-grey); }
  .cover__title {
    font-size: 50px;
    font-weight: 400;
    line-height: 1;
    letter-spacing: 3px;
    text-transform: uppercase;
    color: var(--ink-black);
    white-space: nowrap;
    transform: scale(0.7, 1.25);
  }
</style>
</head>
<body>
  <main class="cover-set">
    <article class="cover cover--one">
      <div class="cover__photo" role="img" aria-label="Moody black and white photo of a woman's lower face and bob hair, fading into black"></div>
      <p class="cover__author">Lydia K Barnes</p>
      <p class="cover__series">Short Story</p>
      <div class="cover__title-band"><h2 class="cover__title">First Crow</h2></div>
    </article>

    <article class="cover cover--two">
      <div class="cover__photo" role="img" aria-label="Red-tinted photo of a woman's lower face and bob hair, fading into burgundy"></div>
      <p class="cover__author">Lydia K Barnes</p>
      <p class="cover__series">Short Story</p>
      <div class="cover__title-band"><h2 class="cover__title">Second Crow</h2></div>
    </article>

    <article class="cover cover--three">
      <div class="cover__photo" role="img" aria-label="Grey-toned photo of a woman's lower face and bob hair, fading into charcoal"></div>
      <p class="cover__author">Lydia K Barnes</p>
      <p class="cover__series">Short Story</p>
      <div class="cover__title-band"><h2 class="cover__title">Third Crow</h2></div>
    </article>
  </main>
</body>
</html>
```